Basic images needed for business powerpoint slides

We need basic images for a powerpoint design. The designs should be clean, modern, simple and easy to read on a screen and if they were printed on paper. The images should not be overly designed (no fancy graphics or ornate fonts), but should still look professional.

Please pay attention to the attachments that have sketches of the images that are needed. In the notes section of the powerpoint slides specifies additional details for each image.

Also, please adhere to the design guidelines that are also uploaded. Only use colors and fonts that are specified. The final images should be similar to the look and feel of the images in the design guidelines.
Updates

Designers -
Thanks for all your submissions! I am reviewing all the designs with my team and will have a decision ready by Sunday evening. If you are submitting any new designs, please submit by Sunday morning EST so my team can review them.

Thanks!

Target Market(s)

business executives

Industry/Entity Type

Business

Requirements
Must have
• Must Have:
- 1. Please see the attached powerpoint for the sketches we would like to have recreated. There are specific notes in each slide with additional details.

2. Please refer to the following pages in the uploaded design guideline document:
Colors - p. 14
- Use either the bright or muted color options as specified in the color scheme on this page

Typography - p. 16-17
- Use either helvetica or arial options

Powerpoint guidelines - p.42
- see for example of the general look and feel of the company

```html
<!DOCTYPE html>
<html lang="en">
<head>
<meta charset="utf-8">
<title>Internal Stakeholder Rings</title>
<link rel="stylesheet" href="https://fonts.googleapis.com/css2?family=Arimo:wght@400;700&display=swap">
<style>
  :root {
    --canvas-bg: #cbcbcb;
    --ring-outer: #2e9ad9;
    --ring-outer-dark: #1f86c8;
    --ring-orange: #f28a1e;
    --ring-orange-dark: #e06f0c;
    --ring-navy: #2361ad;
    --ring-navy-dark: #1a4f94;
    --core-yellow: #fdc81a;
    --core-yellow-light: #ffd84a;
    --ink: #1b2a4a;
    --ink-light: #ffffff;
    --divider: #ffffff;
  }
  html, body {
    margin: 0;
    padding: 0;
    overflow: hidden;
    background: var(--canvas-bg);
  }
  .slide {
    position: relative;
    width: 1200px;
    height: 900px;
    overflow: hidden;
    background: var(--canvas-bg);
    font-family: "Arimo", Arial, Helvetica, sans-serif;
  }
  .slide-title {
    position: absolute;
    left: 200px;
    top: 18px;
    margin: 0;
    font-size: 30px;
    font-weight: 700;
    color: #000;
  }
  .rings {
    position: absolute;
    left: 0;
    top: 0;
  }
  .ring-label {
    font-size: 32px;
    fill: var(--ink);
  }
  .ring-label--light { fill: var(--ink-light); }
  .ring-label .num { font-weight: 700; }
  .group-num {
    font-size: 34px;
    font-weight: 700;
    fill: var(--ink);
  }
  .group-text {
    font-size: 16px;
    fill: var(--ink);
  }
  .group-text .strong { font-weight: 700; }
  .align-end { text-anchor: end; }
  .align-start { text-anchor: start; }
  .align-middle { text-anchor: middle; }
  .divider {
    stroke: var(--divider);
    stroke-width: 5;
  }
</style>
</head>
<body>
<div class="slide">
  <h1 class="slide-title">Internal</h1>

  <svg class="rings" width="1200" height="900" viewBox="0 0 1200 900" xmlns="http://www.w3.org/2000/svg">
    <defs>
      <radialGradient id="grad-outer" cx="608" cy="450" r="429" gradientUnits="userSpaceOnUse">
        <stop offset="0.8" stop-color="var(--ring-outer-dark)"/>
        <stop offset="0.88" stop-color="var(--ring-outer)"/>
        <stop offset="1" stop-color="var(--ring-outer)"/>
      </radialGradient>
      <radialGradient id="grad-orange" cx="608" cy="450" r="343" gradientUnits="userSpaceOnUse">
        <stop offset="0.78" stop-color="var(--ring-orange-dark)"/>
        <stop offset="0.9" stop-color="var(--ring-orange)"/>
        <stop offset="1" stop-color="var(--ring-orange)"/>
      </radialGradient>
      <radialGradient id="grad-navy" cx="608" cy="450" r="269" gradientUnits="userSpaceOnUse">
        <stop offset="0.72" stop-color="var(--ring-navy-dark)"/>
        <stop offset="0.86" stop-color="var(--ring-navy)"/>
        <stop offset="1" stop-color="var(--ring-navy)"/>
      </radialGradient>
      <radialGradient id="grad-core" cx="608" cy="450" r="196" gradientUnits="userSpaceOnUse">
        <stop offset="0" stop-color="var(--core-yellow-light)"/>
        <stop offset="1" stop-color="var(--core-yellow)"/>
      </radialGradient>

      <path id="arc-outer" d="M 230,450 A 378 378 0 0 1 986,450"/>
      <path id="arc-orange" d="M 318,450 A 290 290 0 0 1 898,450"/>
      <path id="arc-navy-top" d="M 388,450 A 220 220 0 0 1 828,450"/>
      <path id="arc-navy-bottom" d="M 373,450 A 235 235 0 0 0 843,450"/>
    </defs>

    <circle class="ring ring--outer" cx="608" cy="450" r="429" fill="url(#grad-outer)"/>
    <circle class="ring ring--orange" cx="608" cy="450" r="343" fill="url(#grad-orange)"/>
    <circle class="ring ring--navy" cx="608" cy="450" r="269" fill="url(#grad-navy)"/>
    <circle class="core" cx="608" cy="450" r="196" fill="url(#grad-core)"/>

    <line class="divider" x1="340" y1="449" x2="878" y2="449"/>
    <line class="divider" x1="608" y1="254" x2="608" y2="646"/>

    <text class="ring-label">
      <textPath href="#arc-outer" startOffset="50%" text-anchor="middle"><tspan class="num">9.</tspan> Franchise Lawyers • Finance</textPath>
    </text>
    <text class="ring-label">
      <textPath href="#arc-orange" startOffset="50%" text-anchor="middle"><tspan class="num">8.</tspan> Legal Analysts</textPath>
    </text>
    <text class="ring-label ring-label--light">
      <textPath href="#arc-navy-top" startOffset="50%" text-anchor="middle"><tspan class="num">7.</tspan> Sales &amp; Marketing</textPath>
    </text>
    <text class="ring-label">
      <textPath href="#arc-navy-bottom" startOffset="50%" text-anchor="middle"><tspan class="num">6.</tspan> Scientists</textPath>
    </text>

    <g class="group group--1">
      <text class="group-num" x="434" y="424">1.</text>
      <text class="group-text align-end">
        <tspan class="strong" x="598" y="361">HFAC</tspan>
        <tspan class="strong" x="598" y="383">Specialists</tspan>
        <tspan x="598" y="405">(Med Products</tspan>
        <tspan x="598" y="427">– Commercial)</tspan>
      </text>
    </g>

    <g class="group group--2">
      <text class="group-num" x="620" y="428">2.</text>
      <text class="group-text align-start">
        <tspan class="strong" x="660" y="361">HFAC</tspan>
        <tspan class="strong" x="660" y="383">Specialists</tspan>
        <tspan x="660" y="405">(Bio Science –</tspan>
        <tspan x="660" y="427">Commercial)</tspan>
      </text>
    </g>

    <g class="group group--3">
      <text class="group-num" x="430" y="494">3.</text>
      <text class="group-text align-end">
        <tspan class="strong" x="598" y="477">HFAC Specialists</tspan>
        <tspan x="598" y="499">(Med Products –</tspan>
        <tspan x="598" y="521">Med Affairs)</tspan>
      </text>
    </g>

    <g class="group group--4">
      <text class="group-num" x="620" y="494">4.</text>
      <text class="group-text align-start">
        <tspan class="strong" x="657" y="477">HFAC Specialists</tspan>
        <tspan x="660" y="499">(Bio Science –</tspan>
        <tspan x="670" y="521">Med Affairs)</tspan>
      </text>
    </g>

    <g class="group group--5">
      <text class="group-num" x="620" y="568">5.</text>
      <text class="group-text align-start">
        <tspan class="strong" x="660" y="548">HFAC</tspan>
        <tspan class="strong" x="657" y="570">Specialists</tspan>
        <tspan x="657" y="592">(Clinical</tspan>
        <tspan x="660" y="614">Trials)</tspan>
      </text>
    </g>
  </svg>
</div>
</body>
</html>
```